Business Card Design for Varnok Facility Services

We are looking for a Business Card Design for the Company "Varnok Facility Services."
Front side:
- Company Logo (small)
- Company Name, address, pohone, website and personal data.
- white background, for text e.g. company colors (blue or green like in the logo)
Please use following data:
Company data:
Varnok Facility Services Tulbrecht
Kirchmattweg 12
6331 Cham
www.varnok-fs.ch
Person data:
Ruben Tulbrecht
Geschäftsführer
+41 76 519 84 60
info@varnok-fs.ch
Back side:
could be colored in blue or green
please use a big logo sing and some smaller icons to say what is all beeing offered in facility services, like cleaning, maintenance cleaning
industrial cleaning, caretaking, gardening, disposal. There is no need for everyone of the icons if there are similar or an icon is standing for more of them.
Cleaning Service
colors to use:
blue: HEX 246BB0
green: HEX 52B33E

```html
<!DOCTYPE html>
<html lang="de">
<head>
<meta charset="utf-8">
<title>Varnok Facility Services – Visitenkarte</title>
<link rel="stylesheet" href="https://fonts.googleapis.com/css2?family=Lato:wght@400;700&display=swap">
<style>
  :root {
    --brand-blue: #246BB0;
    --brand-green: #52B33E;
    --text-grey: #6b6b6b;
    --paper: #ffffff;
    --backdrop: #e9e7e4;
  }
  * { box-sizing: border-box; margin: 0; padding: 0; }
  html, body {
    width: 1200px; height: 848px; overflow: hidden;
    background: var(--backdrop);
    font-family: "Lato", sans-serif;
  }
  .canvas { position: relative; width: 1200px; height: 848px; }
  .card {
    position: absolute; left: 264px; width: 672px; height: 380px;
    box-shadow: 0 6px 18px rgba(0,0,0,0.18);
  }
  .card--front { top: 28px; background: var(--paper); }
  .card--back { top: 440px; background: var(--brand-blue); color: #fff; }

  /* front */
  .wordmark {
    position: absolute; display: flex; align-items: center; gap: 10px;
    font-weight: 700; color: var(--brand-blue);
  }
  .wordmark__dot { flex: none; border-radius: 50%; background: currentColor; }
  .card--front .wordmark { left: 92px; top: 150px; width: 250px; font-size: 22px; line-height: 1.15; }
  .card--front .wordmark__dot { width: 18px; height: 18px; background: var(--brand-green); }
  .divider {
    position: absolute; left: 354px; top: 99px; width: 2px; height: 184px;
    background: var(--brand-blue);
  }
  .contact { position: absolute; left: 377px; top: 92px; color: var(--text-grey); }
  .contact__name { font-size: 20px; font-weight: 700; color: var(--brand-blue); line-height: 24px; }
  .contact__role { font-size: 17px; line-height: 22px; }
  .contact__address { margin-top: 17px; font-size: 17px; line-height: 23px; }
  .contact__list { list-style: none; margin-top: 17px; font-size: 17px; line-height: 23px; }
  .contact__list li { display: flex; align-items: center; gap: 8px; }
  .contact__list svg { width: 12px; height: 12px; fill: var(--brand-blue); flex: none; }

  /* back */
  .card--back .wordmark {
    left: 0; right: 0; top: 96px; justify-content: center;
    color: #fff; font-size: 40px; letter-spacing: 1px;
  }
  .card--back .wordmark__dot { width: 30px; height: 30px; }
  .services { position: absolute; left: 0; right: 0; top: 236px; text-align: center; }
  .services__title {
    display: inline-block; font-size: 27px; font-weight: 700;
    padding: 0 6px 5px; border-bottom: 2px solid #fff;
  }
  .services__row {
    list-style: none; display: flex; justify-content: center; gap: 14px;
    font-size: 21px; line-height: 31px;
  }
  .services__row:first-of-type { margin-top: 8px; }
  .services__row li::before {
    content: ""; display: inline-block; width: 11px; height: 11px;
    border-radius: 50%; background: #fff; margin-right: 9px; vertical-align: middle;
  }
</style>
</head>
<body>
<main class="canvas">
  <section class="card card--front" aria-label="Vorderseite">
    <div class="wordmark">
      <span class="wordmark__dot"></span>
      <span>Varnok Facility Services</span>
    </div>
    <div class="divider"></div>
    <div class="contact">
      <p class="contact__name">Ruben Tulbrecht</p>
      <p class="contact__role">Geschäftsführer</p>
      <p class="contact__address">Kirchmattweg 12<br>6331 Cham</p>
      <ul class="contact__list">
        <li>
          <svg viewBox="0 0 24 24" aria-hidden="true"><path d="M6.6 10.8a15 15 0 0 0 6.6 6.6l2.2-2.2a1 1 0 0 1 1-.25 11.4 11.4 0 0 0 3.6.57 1 1 0 0 1 1 1V20a1 1 0 0 1-1 1A17 17 0 0 1 3 4a1 1 0 0 1 1-1h3.5a1 1 0 0 1 1 1c0 1.25.2 2.45.57 3.57a1 1 0 0 1-.25 1z"/></svg>
          +41 76 519 84 60
        </li>
        <li>
          <svg viewBox="0 0 24 24" aria-hidden="true"><path d="M2 5h20v14H2z M3 6l9 7 9-7" fill-rule="evenodd"/></svg>
          info@varnok-fs.ch
        </li>
        <li>
          <svg viewBox="0 0 24 24" aria-hidden="true"><circle cx="12" cy="12" r="10" fill="none" stroke="#246BB0" stroke-width="2"/><path d="M2 12h20M12 2c3 3 3 17 0 20M12 2c-3 3-3 17 0 20" fill="none" stroke="#246BB0" stroke-width="1.6"/></svg>
          www.varnok-fs.ch
        </li>
      </ul>
    </div>
  </section>

  <section class="card card--back" aria-label="Rückseite">
    <div class="wordmark">
      <span class="wordmark__dot"></span>
      <span>Varnok Facility Services</span>
    </div>
    <div class="services">
      <h2 class="services__title">Services</h2>
      <ul class="services__row">
        <li>Maintenance cleaning</li>
        <li>Industrial cleaning</li>
      </ul>
      <ul class="services__row">
        <li>Cleaning</li>
        <li>Caretaking</li>
        <li>Gardening, disposal</li>
      </ul>
    </div>
  </section>
</main>
</body>
</html>
```